General Contractors need a new Crisp updated Card Design

We need a new business card design for our company of 25 years based in Toronto call Holvaster Building Inc. : Our goal is to be the leading commercial contractors in Toronto by providing exceptional value to our clients. We work very hard to deliver professional, quality, service in conjunction with consistent price competitiveness to all of our clients on every single project.

Target Market(s)

Design & Build Clients

Industry/Entity Type

Construction Company

Contact Information for Business Card

Address:
18 North Tamlin Glen Road, Unit 57, Marbrook Vale, ON, K7T 2R9
Office: 905-218-5937

Holvasters Logo
Employee Job Description
Employee Cell Phone #
Employee Email
www.holvaster-example.com

Colors

Designer to choose colors to be used in the design.

Requirements
Must have
• Quote Company Saying:
• "Professional. Quality. Service."
Nice to have
• New Crisp up to date look. simple & fresh ( Not to Busy)
Should not have
• NO BLUE PRINTS ON THE BUSINESS CARDS

```html
<!DOCTYPE html>
<html lang="en">
<head>
<meta charset="utf-8">
<title>Holvaster Building Inc. – Business Card</title>
<link href="https://fonts.googleapis.com/css2?family=Lato:wght@400;700&family=Montserrat:wght@400;700&display=swap" rel="stylesheet">
<style>
  :root {
    --teal: #00796f;
    --teal-soft: #2aa39a;
    --ink: #3a3a3a;
    --card-black: #141414;
    --paper: #ffffff;
    --backdrop: #e6e6e6;
  }
  * { box-sizing: border-box; margin: 0; padding: 0; }
  html, body { width: 1200px; height: 716px; overflow: hidden; }
  body {
    background: var(--backdrop);
    position: relative;
    font-family: "Lato", Arial, sans-serif;
  }
  .card {
    position: absolute;
    top: 208px;
    width: 530px;
    height: 300px;
    border-radius: 18px;
    overflow: hidden;
    box-shadow: 0 6px 18px rgba(0,0,0,0.18);
  }

  /* Back side */
  .card-back {
    left: 45px;
    background: var(--card-black);
    display: flex;
    flex-direction: column;
    align-items: center;
    justify-content: center;
  }
  .brand {
    display: flex;
    align-items: center;
    gap: 14px;
  }
  .brand-mark {
    width: 30px;
    height: 30px;
    background: var(--teal-soft);
    flex: none;
  }
  .brand-name {
    font-family: "Lato", Arial, sans-serif;
    font-weight: 700;
    font-size: 28px;
    letter-spacing: 2px;
    color: var(--teal-soft);
    white-space: nowrap;
  }
  .back-web {
    margin-top: 32px;
    font-size: 14px;
    letter-spacing: 4px;
    color: var(--teal-soft);
    text-transform: uppercase;
  }
  .slogan {
    margin-top: 12px;
    font-size: 12px;
    letter-spacing: 2px;
    color: var(--teal-soft);
  }

  /* Front side */
  .card-front {
    left: 625px;
    background: var(--paper);
  }
  .identity {
    position: absolute;
    left: 34px;
    top: 40px;
    width: 320px;
    padding-bottom: 8px;
    border-bottom: 2px solid var(--teal);
  }
  .person-name {
    font-family: "Montserrat", Arial, sans-serif;
    font-weight: 700;
    font-size: 21px;
    color: var(--teal);
    line-height: 1;
  }
  .job-title {
    font-family: "Montserrat", Arial, sans-serif;
    font-size: 14px;
    color: var(--teal);
    margin-top: 2px;
  }
  .contact-list {
    position: absolute;
    left: 34px;
    top: 116px;
    width: 340px;
    list-style: none;
  }
  .contact-item {
    display: flex;
    align-items: flex-start;
    gap: 10px;
    font-size: 13px;
    line-height: 18px;
    color: var(--ink);
    margin-bottom: 10px;
  }
  .contact-icon {
    width: 18px;
    height: 18px;
    flex: none;
  }
  .brand-band {
    position: absolute;
    right: 0;
    top: 0;
    width: 112px;
    height: 100%;
    background: var(--teal);
  }
  .band-brand {
    position: absolute;
    left: 50%;
    top: 50%;
    transform: translate(-50%, -50%) rotate(-90deg);
    display: flex;
    align-items: center;
    gap: 12px;
    white-space: nowrap;
  }
  .band-brand .brand-mark {
    width: 26px;
    height: 26px;
    background: var(--paper);
  }
  .band-lines { display: flex; flex-direction: column; line-height: 1.05; }
  .band-brand .brand-name {
    font-size: 24px;
    letter-spacing: 1.5px;
    color: var(--paper);
  }
  .band-brand .brand-sub {
    font-family: "Lato", Arial, sans-serif;
    font-weight: 700;
    font-size: 13px;
    letter-spacing: 3px;
    color: var(--paper);
  }
</style>
</head>
<body>

<section class="card card-back" aria-label="Card back">
  <div class="brand">
    <span class="brand-mark"></span>
    <span class="brand-name">HOLVASTER BUILDING INC.</span>
  </div>
  <p class="back-web">www.holvaster-example.com</p>
  <p class="slogan">Professional. Quality. Service.</p>
</section>

<section class="card card-front" aria-label="Card front">
  <div class="identity">
    <h1 class="person-name">YOUR NAME</h1>
    <p class="job-title">Job Title</p>
  </div>

  <ul class="contact-list">
    <li class="contact-item">
      <svg class="contact-icon" viewBox="0 0 18 18"><circle cx="9" cy="9" r="8" fill="none" stroke="var(--teal)" stroke-width="1.2"/><path d="M6.2 5.2l1.6-.4.9 2-1 .8a5 5 0 0 0 2.7 2.7l.8-1 2 .9-.4 1.6c-3.8.2-6.8-2.8-6.6-6.6z" fill="var(--teal)"/></svg>
      <span>905-218-5937</span>
    </li>
    <li class="contact-item">
      <svg class="contact-icon" viewBox="0 0 18 18"><circle cx="9" cy="9" r="8" fill="none" stroke="var(--teal)" stroke-width="1.2"/><rect x="6.5" y="4.5" width="5" height="9" rx="1" fill="none" stroke="var(--teal)" stroke-width="1.1"/><circle cx="9" cy="11.8" r=".6" fill="var(--teal)"/></svg>
      <span>000 000 0000</span>
    </li>
    <li class="contact-item">
      <svg class="contact-icon" viewBox="0 0 18 18"><circle cx="9" cy="9" r="8" fill="none" stroke="var(--teal)" stroke-width="1.2"/><rect x="5" y="5.5" width="8" height="5.5" fill="none" stroke="var(--teal)" stroke-width="1.1"/><path d="M7 13h4M9 11v2" stroke="var(--teal)" stroke-width="1.1"/></svg>
      <span>www.holvaster-example.com</span>
    </li>
    <li class="contact-item">
      <svg class="contact-icon" viewBox="0 0 18 18"><circle cx="9" cy="9" r="8" fill="none" stroke="var(--teal)" stroke-width="1.2"/><rect x="5" y="6" width="8" height="6" fill="var(--teal)"/><path d="M5 6l4 3.2L13 6" fill="none" stroke="#fff" stroke-width=".9"/></svg>
      <span>youremail@holvaster-example.com</span>
    </li>
    <li class="contact-item">
      <svg class="contact-icon" viewBox="0 0 18 18"><circle cx="9" cy="9" r="8" fill="none" stroke="var(--teal)" stroke-width="1.2"/><path d="M9 14s-3.2-3.4-3.2-5.6a3.2 3.2 0 0 1 6.4 0C12.2 10.6 9 14 9 14z" fill="var(--teal)"/><circle cx="9" cy="8.4" r="1.1" fill="#fff"/></svg>
      <span>18 North Tamlin Glen Road, Unit 57,<br>Marbrook Vale, ON, K7T 2R9</span>
    </li>
  </ul>

  <div class="brand-band">
    <div class="band-brand">
      <span class="brand-mark"></span>
      <span class="band-lines">
        <span class="brand-name">HOLVASTER</span>
        <span class="brand-sub">BUILDING INC.</span>
      </span>
    </div>
  </div>
</section>

</body>
</html>
```